Creative/innovative law firm website

A law firm website that immediately looks different from other law firm websites. We like the color scheme (dark background with warm, neutral colors) and simple, organic logos (trees, leaves, etc.) of this website: https://brambleworth.legal/

We'll be offering creative/innovative solutions to complex problems faced by state governments, industries, other law firms, and individuals. We're located in Montana (U.S.A.), and the outdoors is a huge part of our lives and identities.

We will need a home page, an "About Us" page with a separate subpage for each attorney (two attorneys), a blog or "Publications" page, a payment portal (which will integrate with Quillo), and a "Services" page.

```html
<!DOCTYPE html>
<html lang="en">
<head>
<meta charset="utf-8">
<title>Law Firm</title>
<link href="https://fonts.googleapis.com/css2?family=Poppins:wght@400;500;600&family=Arimo:wght@400;700&display=swap" rel="stylesheet">
<style>
:root{
  --black:#000;
  --panel:#111111;
  --card:#1b1b1b;
  --field:#181818;
  --orange:#e0861e;
  --white:#fff;
  --muted:#d6d6d6;
  --line:#2a2a2a;
}
*{margin:0;padding:0;box-sizing:border-box}
html,body{width:1200px;height:3826px;overflow:hidden;background:var(--black)}
body{position:relative;font-family:"Arimo",Arial,sans-serif;color:var(--white)}
.abs{position:absolute}
.head{font-family:"Poppins",sans-serif;font-weight:600}
a{color:inherit;text-decoration:none}

/* header */
.header{left:0;top:0;width:1200px;height:106px;background:var(--black)}
.brand{left:110px;top:22px;font-size:42px;line-height:54px}
.topbar{left:393px;top:0;width:807px;height:37px;background:var(--orange);clip-path:polygon(0 0,100% 0,100% 100%,36px 100%)}
.topbar span{position:absolute;top:9px;font-size:15px;color:var(--white);display:flex;align-items:center;gap:6px;white-space:nowrap}
.dot{width:12px;height:12px;border-radius:50%;border:1.5px solid var(--white);display:inline-block}
.nav{top:58px;font-size:16px;font-family:"Poppins",sans-serif}
.nav a.active{color:var(--orange)}
.nav-underline{left:469px;top:103px;width:46px;height:3px;background:var(--orange)}

/* hero */
.hero-box{left:111px;top:278px;width:520px;height:279px;background:rgba(40,40,40,.72);border-radius:14px}
.hero-title{left:130px;top:312px;font-size:41px;white-space:nowrap}
.hero-text{left:129px;top:383px;width:480px;font-size:15px;line-height:30px;color:var(--muted)}
.btn{background:var(--orange);color:var(--white);border-radius:26px;font-family:"Poppins",sans-serif;font-weight:500;font-size:15px;display:flex;align-items:center;justify-content:center}

/* sections */
.section-title{width:1200px;left:0;text-align:center;font-size:36px}
.intro{left:285px;top:945px;width:630px;text-align:center;font-size:15px;line-height:25.5px;color:var(--muted)}
.service-img{top:1057px;width:216px;height:205px}
.service-label{top:1275px;width:216px;text-align:center;font-size:19px}
.about-bg{left:0;top:1381px;width:1200px;height:569px;background:var(--panel)}
.about-text{left:113px;top:1592px;width:460px;font-size:15px;line-height:28px;color:var(--muted)}
.frame{left:603px;top:1466px;width:486px;height:398px;background:var(--white);padding:9px}

.blog-card{top:2128px;width:314px;height:514px;background:var(--card);border-radius:6px;overflow:hidden}
.blog-img{width:314px;height:245px}
.date{top:-4px;left:19px;width:42px;height:53px;background:var(--orange);font-family:"Poppins",sans-serif;font-weight:500;font-size:15px;line-height:20px;text-align:center;padding-top:6px}
.blog-title{left:12px;top:260px;width:295px;font-size:19px;line-height:27px}
.blog-text{left:12px;top:328px;width:285px;font-size:14.5px;line-height:30px;color:var(--muted)}
.read{left:12px;top:465px;font-family:"Poppins",sans-serif;font-weight:600;font-size:15px;color:var(--orange);border-bottom:2px solid var(--orange);padding-bottom:2px}

.contact-bg{left:0;top:2729px;width:1200px;height:716px;background:var(--panel)}
.field{left:171px;width:415px;background:var(--field);font-size:15px;color:var(--muted);padding:18px 0 0 28px}
.info-icon{left:710px;width:44px;height:44px;border-radius:50%;background:var(--orange);display:flex;align-items:center;justify-content:center}
.info-label{left:781px;font-family:"Poppins",sans-serif;font-weight:600;font-size:16px}
.info-text{left:781px;font-size:15px;line-height:24px;color:var(--muted);white-space:nowrap}

.footer-title{font-size:19px}
.footer-item{font-size:15px;color:var(--muted);display:flex;gap:10px;align-items:flex-start;line-height:24px;white-space:nowrap}
.social{top:3586px;width:36px;height:36px;border-radius:50%;border:1.5px solid var(--white)}
.divider{left:111px;top:3732px;width:978px;height:1px;background:var(--line)}
.copyright{left:0;top:3766px;width:1200px;text-align:center;font-size:15px;color:var(--muted)}
</style>
</head>
<body>

<!-- hero photo and chevron -->
<svg class="abs" style="left:0;top:0" width="1200" height="810" viewBox="0 0 1200 810">
  <defs>
    <linearGradient id="heroTone" x1="0" y1="0" x2="1" y2="1">
      <stop offset="0" stop-color="#4a4640"/>
      <stop offset=".5" stop-color="#6b4a2e"/>
      <stop offset="1" stop-color="#2b1d14"/>
    </linearGradient>
  </defs>
  <polygon points="270,700 600,802 1060,700 600,780" fill="#e0861e"/>
  <g role="img" aria-label="Team meeting around a wooden conference table in a brick-walled office">
    <polygon points="0,106 1200,106 1200,700 600,788 0,700" fill="url(#heroTone)"/>
  </g>
</svg>

<header class="abs header"></header>
<div class="abs brand head">Law Firm</div>
<div class="abs topbar">
  <span style="left:75px">&#9742; 406-555-0142</span>
  <span style="left:231px">&#9993; info@ridgelinelaw.example</span>
  <span style="left:505px">&#10140; Login</span>
  <span style="left:599px;gap:12px"><i class="dot"></i><i class="dot"></i><i class="dot"></i><i class="dot"></i></span>
</div>
<nav>
  <a class="abs nav active" style="left:469px">Home</a>
  <a class="abs nav" style="left:566px">About us</a>
  <a class="abs nav" style="left:683px">Services</a>
  <a class="abs nav" style="left:796px">Publications</a>
  <a class="abs nav" style="left:940px">Blog</a>
  <a class="abs nav" style="left:1023px">Contact</a>
</nav>
<div class="abs nav-underline"></div>

<div class="abs hero-box"></div>
<h1 class="abs hero-title head">Welcome To Law Firm</h1>
<p class="abs hero-text">Lorem ipsum dolor sit amet, consectetur adipiscing elit, sed do eius-mod tempor incididunt ut labore et dolore magna aliqua.</p>
<a class="abs btn" style="left:126px;top:475px;width:150px;height:50px">Learn More</a>

<!-- services -->
<h2 class="abs section-title head" style="top:878px">Law Firm Services</h2>
<p class="abs intro">Lorem ipsum dolor sit amet, consectetur adipiscing elit, sed do eiusmod tempor incididunt ut labore et dolore magna aliqua. Quis ipsum suspendisse ultrices gravida. Risus commodo viverra maecenas accumsan lacus vel facilisis.</p>
<div class="abs service-img" role="img" aria-label="Colleagues reviewing documents at a table" style="left:137px;background:linear-gradient(135deg,#8a7b6a,#4f4036)"></div>
<div class="abs service-img" role="img" aria-label="Hands at a laptop showing charts" style="left:374px;background:linear-gradient(135deg,#b8b8b8,#6e6e6e);border:4px solid var(--orange)"></div>
<div class="abs service-img" role="img" aria-label="Business group seated at a meeting table" style="left:610px;background:linear-gradient(135deg,#6c6a58,#3a3a30)"></div>
<div class="abs service-img" role="img" aria-label="Two professionals talking with a tablet" style="left:848px;background:linear-gradient(135deg,#7c6e64,#3e3431)"></div>
<div class="abs service-label head" style="left:137px">State Governments</div>
<div class="abs service-label head" style="left:374px">Industries</div>
<div class="abs service-label head" style="left:610px">Law Firms</div>
<div class="abs service-label head" style="left:848px">Individuals</div>

<!-- about -->
<div class="abs about-bg"></div>
<h2 class="abs head" style="left:113px;top:1528px;font-size:36px">About Law Firm</h2>
<p class="abs about-text">Lorem ipsum dolor sit amet, consectetur adipiscing elit, sed do eiusmod tempor incididunt ut labore et dolore magna aliqua. Quis ipsum suspendisse ultrices gravida. Risus commodo viverra maecenas accumsan lacus vel facilisis.</p>
<a class="abs btn" style="left:110px;top:1729px;width:150px;height:50px">Learn More</a>
<div class="abs frame"><div role="img" aria-label="Team meeting in a glass-walled modern office" style="width:100%;height:100%;background:linear-gradient(135deg,#6f86a4,#263448)"></div></div>

<!-- blog -->
<h2 class="abs section-title head" style="top:2026px">Latest Blog</h2>
<article class="abs blog-card" style="left:113px">
  <div class="blog-img" role="img" aria-label="Colleagues shaking hands over a desk" style="background:linear-gradient(135deg,#a7a9ad,#55585e)"></div>
  <div class="abs date">06<br>DEC</div>
  <h3 class="abs blog-title head">Lorem ipsum dolor sit amet consectetur</h3>
  <p class="abs blog-text">Lorem ipsum dolor sit amet, consectetur adipiscing elit, sed do eiusmod tempor incididunt ut labore et dolore magna aliqua. Quis ipsum suspendisse</p>
  <a class="abs read">Read More</a>
</article>
<article class="abs blog-card" style="left:444px">
  <div class="blog-img" role="img" aria-label="Presenter at a whiteboard with seated team" style="background:linear-gradient(135deg,#d2d0cc,#6b6660)"></div>
  <div class="abs date">06<br>DEC</div>
  <h3 class="abs blog-title head">Lorem ipsum dolor sit amet consectetur</h3>
  <p class="abs blog-text">Lorem ipsum dolor sit amet, consectetur adipiscing elit, sed do eiusmod tempor incididunt ut labore et dolore magna aliqua. Quis ipsum suspendisse</p>
  <a class="abs read">Read More</a>
</article>
<article class="abs blog-card" style="left:774px">
  <div class="blog-img" role="img" aria-label="Two colleagues reviewing a tablet" style="background:linear-gradient(135deg,#4c5560,#1f242a)"></div>
  <div class="abs date">06<br>DEC</div>
  <h3 class="abs blog-title head">Lorem ipsum dolor sit amet consectetur</h3>
  <p class="abs blog-text">Lorem ipsum dolor sit amet, consectetur adipiscing elit, sed do eiusmod tempor incididunt ut labore et dolore magna aliqua. Quis ipsum suspendisse</p>
  <a class="abs read">Read More</a>
</article>

<!-- contact -->
<div class="abs contact-bg"></div>
<h2 class="abs head" style="left:171px;top:2797px;font-size:36px">Contact Us</h2>
<div class="abs field" style="top:2888px;height:52px">Name</div>
<div class="abs field" style="top:2955px;height:54px">Email</div>
<div class="abs field" style="top:3022px;height:54px">Phone Number</div>
<div class="abs field" style="top:3089px;height:86px">Type Your Message</div>
<a class="abs btn" style="left:171px;top:3185px;width:415px;height:54px;border-radius:3px;font-weight:600">Submit</a>

<div class="abs info-icon" style="top:2953px"><svg width="14" height="18" viewBox="0 0 14 18"><path d="M7 0a7 7 0 0 0-7 7c0 5 7 11 7 11s7-6 7-11a7 7 0 0 0-7-7zm0 9.5A2.5 2.5 0 1 1 7 4.5a2.5 2.5 0 0 1 0 5z" fill="#fff"/></svg></div>
<div class="abs info-label" style="top:2952px">Address</div>
<div class="abs info-text" style="top:2976px">Lorem ipsum dolor sit amet<br>consectetur adipiscing</div>
<div class="abs info-icon" style="top:3046px"><svg width="16" height="16" viewBox="0 0 16 16"><path d="M3 1l3 3-2 2c1 2 3 4 5 5l2-2 3 3-2 3C7 15 1 9 0 3z" fill="#fff"/></svg></div>
<div class="abs info-label" style="top:3048px">Phone</div>
<div class="abs info-text" style="top:3072px">406-555-0188</div>
<div class="abs info-icon" style="top:3123px"><svg width="16" height="12" viewBox="0 0 16 12"><rect width="16" height="12" rx="1.5" fill="#fff"/><path d="M1 1l7 5 7-5" stroke="#e0861e" stroke-width="1.6" fill="none"/></svg></div>
<div class="abs info-label" style="top:3126px">Email</div>
<div class="abs info-text" style="top:3150px;color:var(--orange)">hello@ridgelinelaw.example</div>

<!-- footer -->
<svg class="abs" style="left:0;top:3320px" width="1200" height="506" viewBox="0 0 1200 506">
  <polygon points="0,125 111,125 600,6 1089,125 1200,125 1200,506 0,506" fill="#000"/>
  <polygon points="111,125 600,0 1089,125 600,18" fill="#e0861e"/>
</svg>
<div class="abs head" style="left:190px;top:3502px;font-size:44px">Law Firm</div>
<i class="abs social" style="left:188px"></i>
<i class="abs social" style="left:234px"></i>
<i class="abs social" style="left:279px"></i>
<i class="abs social" style="left:325px"></i>

<div class="abs footer-title head" style="left:522px;top:3483px">Contact Info</div>
<div class="abs footer-item" style="left:524px;top:3528px"><span>&#9906;</span><span>Lorem ipsum dolor sit amet,<br>consectetur adipiscing</span></div>
<div class="abs footer-item" style="left:524px;top:3586px"><span>&#9742;</span><span>406-555-0142</span></div>
<div class="abs footer-item" style="left:524px;top:3624px"><span>&#9993;</span><span>contact@ridgelinelaw.example</span></div>

<div class="abs footer-title head" style="left:872px;top:3483px">Quick Links</div>
<div class="abs footer-item" style="left:876px;top:3527px"><span style="color:var(--orange)">&#187;</span><span>Home</span></div>
<div class="abs footer-item" style="left:876px;top:3557px"><span style="color:var(--orange)">&#187;</span><span>About us</span></div>
<div class="abs footer-item" style="left:876px;top:3587px"><span style="color:var(--orange)">&#187;</span><span>Services</span></div>
<div class="abs footer-item" style="left:876px;top:3617px"><span style="color:var(--orange)">&#187;</span><span>Publications</span></div>
<div class="abs footer-item" style="left:876px;top:3647px"><span style="color:var(--orange)">&#187;</span><span>Blog</span></div>
<div class="abs footer-item" style="left:876px;top:3677px"><span style="color:var(--orange)">&#187;</span><span>Contact</span></div>

<div class="abs divider"></div>
<div class="abs copyright">©Copyrights 2021 Company Name &nbsp;| &nbsp; All Rights Reserved</div>

</body>
</html>
```